Business card design for a dynamic IT consulting company

We need a business card design for a young firm, specialized in the Telecommunications/Consulting industry. The name of the company is Brask and Partners Business Consulting Ltd. (Short name: Brask and Partnes)
Brask = solve read reverse, so we aim to be uncomplicated and solution-oriented. The small pipe in our logo is also related to the word solve. So we need a new business card design, which is simple, eye catching and something non traditional (I would probably prefer a square shaped design rather than a rectangle, but open for suggestions). Attached our logo.

Target Market(s)

Usually our customers are Tier1 Telecoms providers (Q-Linkra, Parnexo, etc) and their executives.

Industry/Entity Type

Business

Contact Information for Business Card

Name: Gergely Halmindo
Email: g.halmindo@braskpartnera.hu
Web: www.braskpartnera.hu
Mobile: +36 30 555 0192
Title: Managing Director

Optional:
Company name: Brask and Partners Ltd.
Address: 1047 Budapest, Ravaszi str. 17/B, Hungary

Font styles to use
Other font styles liked:
• helveticaneue_medium, Prime Regular are used now.

Colors

Designer to choose colors to be used in the design.

Requirements
Must have
• I would like to have a 2 sided design.
Nice to have
• I thought if we make the logo a bit bigger (without the company name), that could go to the back with the company name below. I though, if the pipe in the logo is somehow touchable on the business card, would be nice and unique.

```html
<!DOCTYPE html>
<html lang="en">
<head>
<meta charset="utf-8">
<title>Brask and Partners – Business Card</title>
<link rel="stylesheet" href="https://fonts.googleapis.com/css2?family=Roboto+Condensed:wght@300;400&family=Archivo:wght@900&display=swap">
<style>
  :root {
    --canvas: #ffffff;
    --card: #636466;
    --white: #ffffff;
    --accent-blue: #0a97db;
    --accent-magenta: #b4258f;
    --ink: #333333;
    --body-font: "Roboto Condensed", "Arial Narrow", sans-serif;
  }
  * { margin: 0; padding: 0; box-sizing: border-box; }
  html, body {
    width: 1200px; height: 1000px; overflow: hidden;
    background: var(--canvas);
    font-family: var(--body-font);
  }
  .card {
    position: absolute; left: 206px; width: 788px; height: 451px;
    background: var(--card); color: var(--white);
  }
  .card--front { top: 27px; }
  .card--back { top: 522px; }

  .wordmark {
    position: absolute; left: 0; right: 0;
    display: flex; justify-content: center; align-items: center; gap: 18px;
  }
  .wordmark__square {
    width: 22px; height: 22px; background: var(--accent-blue);
  }
  .wordmark__name {
    font-family: var(--body-font); font-weight: 300;
    font-size: 58px; letter-spacing: 1px; color: var(--white); line-height: 1;
  }
  .card--front .wordmark { top: 42px; }
  .card--back .wordmark { top: 345px; }

  .person { position: absolute; left: 47px; top: 199px; }
  .person__name {
    font-family: "Archivo", var(--body-font); font-weight: 900;
    font-size: 21px; color: var(--accent-blue); line-height: 26px;
  }
  .person__title { font-size: 19px; line-height: 26px; font-weight: 400; }

  .contacts {
    position: absolute; left: 472px; top: 201px; list-style: none;
  }
  .contacts li {
    display: flex; align-items: center; gap: 10px;
    font-size: 19px; height: 32px;
  }
  .contacts svg { width: 18px; height: 18px; flex: none; }

  .address {
    position: absolute; left: 0; right: 0; top: 389px;
    text-align: center; font-size: 19px;
  }
  .company-band {
    position: absolute; left: 211px; width: 365px; top: 421px; height: 20px;
    background: var(--white); color: var(--ink);
    text-align: center; font-size: 18px; line-height: 20px;
  }
  .company-band--wide {
    left: 0; width: 788px; top: 208px; height: 36px; line-height: 36px;
  }
</style>
</head>
<body>

<section class="card card--front" aria-label="Business card front">
  <div class="wordmark">
    <span class="wordmark__square"></span>
    <span class="wordmark__name">Brask &amp; Partners</span>
  </div>

  <div class="person">
    <p class="person__name">Gergely Halmindo</p>
    <p class="person__title">Managing Director</p>
  </div>

  <ul class="contacts">
    <li>
      <svg viewBox="0 0 18 18" aria-hidden="true"><rect x="0.5" y="0.5" width="17" height="17" rx="2" fill="#fff"/><circle cx="9" cy="9" r="5.5" fill="none" stroke="#636466" stroke-width="1.3"/><path d="M7 6.2l1 1.6-.8.7c.4 1 1.2 1.8 2.2 2.3l.7-.8 1.6 1-.6 1.2c-2.3-.4-4.2-2.4-4.6-4.7z" fill="#636466"/></svg>
      +36 30 555 0192
    </li>
    <li>
      <svg viewBox="0 0 18 18" aria-hidden="true"><rect x="0.5" y="0.5" width="17" height="17" rx="2" fill="#fff"/><rect x="3.5" y="5" width="11" height="8" fill="none" stroke="#636466" stroke-width="1.4"/><path d="M3.5 5l5.5 4.5L14.5 5" fill="none" stroke="#636466" stroke-width="1.4"/></svg>
      g.halmindo@braskpartnera.hu
    </li>
    <li>
      <svg viewBox="0 0 18 18" aria-hidden="true"><rect x="0.5" y="0.5" width="17" height="17" rx="2" fill="#fff"/><circle cx="9" cy="9" r="5.5" fill="none" stroke="#636466" stroke-width="1.2"/><ellipse cx="9" cy="9" rx="2.3" ry="5.5" fill="none" stroke="#636466" stroke-width="1"/><path d="M3.5 9h11M4.5 6.3h9M4.5 11.7h9" stroke="#636466" stroke-width="0.9"/></svg>
      www.braskpartnera.hu
    </li>
  </ul>

  <p class="address">1047 Budapest, Ravaszi str. 17/B, Hungary</p>
  <p class="company-band">Brask and Partners Ltd.</p>
</section>

<section class="card card--back" aria-label="Business card back">
  <p class="company-band company-band--wide">Brask and Partners Ltd.</p>
  <div class="wordmark">
    <span class="wordmark__square"></span>
    <span class="wordmark__name">Brask &amp; Partners</span>
  </div>
</section>

</body>
</html>
```